Design a blog page showing lists of latest posts.

I want to design my blog home page. This page will show a list of my latest blog posts.

The site URL is velrunok.com and I have already given a basic structure to it. Please visit and have a look at it.

The color scheme of the design should be black (or grey) and white.

Below the top header I want an opt-in form and below that list of my blog posts. Then pagination and then a bottom section, that will show my two products. Please design these two boxes without any image.

Please avoid using any background image. If necessary, use any image without a character or person. Avoid using the sidebar.

Make it beautiful with the use of typography and white spaces.

I am open to any new creative ideas. Let me know if you have any?

1 page

• Sidebar

```html
<!DOCTYPE html>
<html lang="en">
<head>
<meta charset="utf-8">
<title>Northway Notes — Blog</title>
<link href="https://fonts.googleapis.com/css2?family=Oswald:wght@500;600;700&family=Poppins:wght@400;500;600;700&display=swap" rel="stylesheet">
<style>
:root{
  --ink:#111111;
  --hero:#454545;
  --hero-dark:#3a3a3a;
  --paper:#ffffff;
  --mist:#eef0f2;
  --muted:#7a7a7a;
  --line:#dcdcdc;
  --footer:#0d0d0d;
}
*{box-sizing:border-box;margin:0;padding:0}
html,body{width:684px;height:1200px;overflow:hidden}
body{font-family:'Poppins',sans-serif;color:var(--ink);background:var(--paper);position:relative}
a{color:inherit;text-decoration:none}

/* Hero */
.hero{height:225px;background:linear-gradient(180deg,var(--hero-dark),var(--hero));color:#fff;position:relative}
.topbar{height:40px;display:flex;align-items:center;justify-content:space-between;padding:0 137px}
.brand{font-family:'Poppins',sans-serif;font-weight:600;font-size:10px;color:#fff}
.main-nav{display:flex;gap:11px;font-size:5.5px;font-weight:500;letter-spacing:.3px;text-transform:uppercase}
.hero-title{font-family:'Oswald',sans-serif;font-weight:700;font-size:27px;letter-spacing:1.5px;text-align:center;margin-top:46px}
.hero-sub{font-size:8px;line-height:12px;text-align:center;margin-top:6px;color:#e6e6e6}
.optin{display:flex;justify-content:center;margin-top:16px}
.optin-field{width:200px;height:22px;background:#fff;border:0;font-family:inherit;font-size:5.5px;color:#9a9a9a;padding:0 10px;display:flex;align-items:center}
.optin-button{height:22px;width:78px;background:var(--ink);color:#fff;font-size:5.5px;font-weight:600;letter-spacing:.5px;display:flex;align-items:center;justify-content:center;margin-left:3px}

/* Latest posts */
.latest{height:585px;background:var(--mist);padding-top:70px}
.section-title{font-family:'Oswald',sans-serif;font-weight:600;font-size:14px;letter-spacing:.8px;text-align:center;text-transform:uppercase}
.section-rule{width:22px;height:2px;background:var(--ink);margin:5px auto 0}
.post-grid{width:410px;margin:22px auto 0;display:grid;grid-template-columns:repeat(3,1fr);gap:18px 17px}
.post-card{background:var(--paper);height:168px;box-shadow:0 1px 3px rgba(0,0,0,.08)}
.post-thumb{height:72px}
.thumb-green{background:linear-gradient(135deg,#5cc46a,#2f9e4a)}
.thumb-orange{background:linear-gradient(135deg,#f2b062,#c97b2d)}
.thumb-slate{background:linear-gradient(135deg,#e9edf2,#9fb1c6)}
.thumb-blue{background:linear-gradient(135deg,#6aa8e6,#2e6fb8)}
.thumb-sand{background:linear-gradient(135deg,#f4ead8,#c7b89a)}
.thumb-board{background:linear-gradient(135deg,#2f5a44,#173528)}
.post-body{padding:7px 8px}
.post-meta{display:flex;justify-content:space-between;font-size:4.5px;color:var(--muted);border-bottom:1px solid var(--line);padding-bottom:4px}
.post-title{font-size:7.5px;font-weight:700;line-height:9.5px;margin-top:5px;height:19px}
.post-excerpt{font-size:4.8px;line-height:7px;color:var(--muted);margin-top:4px}
.post-link{display:flex;align-items:center;gap:3px;font-size:4.8px;font-weight:600;margin-top:6px}
.pagination{display:flex;justify-content:center;gap:4px;margin-top:52px}
.page{width:13px;height:13px;display:flex;align-items:center;justify-content:center;font-size:6px;font-weight:600;background:var(--ink);color:#fff}
.page.is-current{background:#fff;color:var(--ink)}

/* Resources */
.resources{padding-top:42px}
.resources-lead{font-size:5.5px;line-height:8px;color:var(--muted);text-align:center;margin-top:8px}
.product-row{display:flex;justify-content:center;gap:20px;margin-top:16px}
.product-box{width:196px;height:136px;border:1px solid var(--line);background:#fff;text-align:center;padding:22px 16px;box-shadow:0 2px 6px rgba(0,0,0,.05)}
.product-name{font-size:8.5px;font-weight:700}
.product-author{font-size:4.8px;color:var(--muted);margin-top:3px}
.product-rule{width:14px;height:1px;background:var(--ink);margin:5px auto}
.product-text{font-size:4.8px;line-height:7px;color:var(--muted)}
.buy-button{display:inline-block;margin-top:11px;background:var(--ink);color:#fff;font-size:5px;font-weight:600;padding:5px 13px;border-radius:10px;letter-spacing:.4px}

/* Footer */
.site-footer{position:absolute;left:0;bottom:0;width:684px;height:92px;background:var(--footer);color:#fff;text-align:center;padding-top:32px}
.footer-nav{display:flex;justify-content:center;gap:16px;font-size:6px;font-weight:500;letter-spacing:.4px}
.copyright{font-size:4.8px;color:#9a9a9a;margin-top:12px}
</style>
</head>
<body>

<header class="hero">
  <div class="topbar">
    <a class="brand" href="#">Northway Notes</a>
    <nav class="main-nav">
      <a href="#">Home</a><a href="#">CPX Certifications</a><a href="#">Resources</a><a href="#">Contact Essays</a><a href="#">Posts</a><a href="#">Login</a>
    </nav>
  </div>
  <h1 class="hero-title">NEVER MISS A POST</h1>
  <p class="hero-sub">In the online marketing space, everybody loves the quick win.<br>The shortcut. The "growth hack".</p>
  <form class="optin">
    <div class="optin-field">Enter your email address</div>
    <div class="optin-button">SUBSCRIBE NOW</div>
  </form>
</header>

<main>
  <section class="latest">
    <h2 class="section-title">Latest Posts</h2>
    <div class="section-rule"></div>
    <div class="post-grid">
      <article class="post-card">
        <div class="post-thumb thumb-green" role="img" aria-label="Green illustration of a crossed-out planning symbol"></div>
        <div class="post-body">
          <div class="post-meta"><span>December 2018</span><span>Exam Guide</span></div>
          <h3 class="post-title">This is an Example of Sample Post</h3>
          <p class="post-excerpt">Lorem ipsum dolor sit amet, consectetur adipiscing elit sed do eiusmod tempor.</p>
          <a class="post-link" href="#">READ <svg width="6" height="4" viewBox="0 0 6 4"><path d="M0 2h5M3.5.5 5 2 3.5 3.5" stroke="#111" fill="none" stroke-width=".7"/></svg></a>
        </div>
      </article>
      <article class="post-card">
        <div class="post-thumb thumb-orange" role="img" aria-label="Orange banner artwork for a training program"></div>
        <div class="post-body">
          <div class="post-meta"><span>December 2018</span><span>Training</span></div>
          <h3 class="post-title">20 Contact Hours Online Risk Pro Training Programs</h3>
          <p class="post-excerpt">Lorem ipsum dolor sit amet, consectetur adipiscing elit sed do eiusmod tempor.</p>
          <a class="post-link" href="#">READ <svg width="6" height="4" viewBox="0 0 6 4"><path d="M0 2h5M3.5.5 5 2 3.5 3.5" stroke="#111" fill="none" stroke-width=".7"/></svg></a>
        </div>
      </article>
      <article class="post-card">
        <div class="post-thumb thumb-slate" role="img" aria-label="Pale blue graphic about a quality method"></div>
        <div class="post-body">
          <div class="post-meta"><span>December 2018</span><span>Methods</span></div>
          <h3 class="post-title">What is Lean Delta?</h3>
          <p class="post-excerpt">Lorem ipsum dolor sit amet, consectetur adipiscing elit sed do eiusmod tempor.</p>
          <a class="post-link" href="#">READ <svg width="6" height="4" viewBox="0 0 6 4"><path d="M0 2h5M3.5.5 5 2 3.5 3.5" stroke="#111" fill="none" stroke-width=".7"/></svg></a>
        </div>
      </article>
      <article class="post-card">
        <div class="post-thumb thumb-blue" role="img" aria-label="Blue comparison graphic of two certifications"></div>
        <div class="post-body">
          <div class="post-meta"><span>December 2018</span><span>Compare</span></div>
          <h3 class="post-title">STRIDE2 vs CPX</h3>
          <p class="post-excerpt">Lorem ipsum dolor sit amet, consectetur adipiscing elit sed do eiusmod tempor.</p>
          <a class="post-link" href="#">READ <svg width="6" height="4" viewBox="0 0 6 4"><path d="M0 2h5M3.5.5 5 2 3.5 3.5" stroke="#111" fill="none" stroke-width=".7"/></svg></a>
        </div>
      </article>
      <article class="post-card">
        <div class="post-thumb thumb-sand" role="img" aria-label="Beige graphic of sample questions and mock tests"></div>
        <div class="post-body">
          <div class="post-meta"><span>December 2018</span><span>Practice</span></div>
          <h3 class="post-title">A List of Free CPX Mock Tests and Sample Questions</h3>
          <p class="post-excerpt">Lorem ipsum dolor sit amet, consectetur adipiscing elit sed do eiusmod tempor.</p>
          <a class="post-link" href="#">READ <svg width="6" height="4" viewBox="0 0 6 4"><path d="M0 2h5M3.5.5 5 2 3.5 3.5" stroke="#111" fill="none" stroke-width=".7"/></svg></a>
        </div>
      </article>
      <article class="post-card">
        <div class="post-thumb thumb-board" role="img" aria-label="Green chalkboard with lessons learned written on it"></div>
        <div class="post-body">
          <div class="post-meta"><span>December 2018</span><span>Stories</span></div>
          <h3 class="post-title">CPX Exam: Lessons Learned by Norvale Exec</h3>
          <p class="post-excerpt">Lorem ipsum dolor sit amet, consectetur adipiscing elit sed do eiusmod tempor.</p>
          <a class="post-link" href="#">READ <svg width="6" height="4" viewBox="0 0 6 4"><path d="M0 2h5M3.5.5 5 2 3.5 3.5" stroke="#111" fill="none" stroke-width=".7"/></svg></a>
        </div>
      </article>
    </div>
    <nav class="pagination">
      <a class="page is-current" href="#">1</a><a class="page" href="#">2</a><a class="page" href="#">›</a>
    </nav>
  </section>

  <section class="resources">
    <h2 class="section-title">Top Recommended Resources</h2>
    <div class="section-rule"></div>
    <p class="resources-lead">Lorem ipsum dolor sit amet, consectetur adipiscing elit, sed do eiusmod tempor<br>incididunt ut labore et dolore magna aliqua. Ut enim ad minim</p>
    <div class="product-row">
      <div class="product-box">
        <h3 class="product-name">The CPX Training Program</h3>
        <p class="product-author">By Tomas Reyel</p>
        <div class="product-rule"></div>
        <p class="product-text">Lorem ipsum dolor sit amet, consectetur adipiscing elit, sed do eiusmod tempor incididunt ut labore et dolore magna aliqua. Ut enim ad minim</p>
        <a class="buy-button" href="#">BUY NOW</a>
      </div>
      <div class="product-box">
        <h3 class="product-name">The CPX Exam Preparation Tool</h3>
        <p class="product-author">By Tomas Reyel</p>
        <div class="product-rule"></div>
        <p class="product-text">Lorem ipsum dolor sit amet, consectetur adipiscing elit, sed do eiusmod tempor incididunt ut labore et dolore magna aliqua. Ut enim ad minim</p>
        <a class="buy-button" href="#">BUY NOW</a>
      </div>
    </div>
  </section>
</main>

<footer class="site-footer">
  <nav class="footer-nav">
    <a href="#">HOME</a><a href="#">CPX</a><a href="#">BOOKS</a><a href="#">ABOUT</a><a href="#">AFFILIATES</a><a href="#">CONTACT</a>
  </nav>
  <p class="copyright">Copyright © 2018 Northway Notes · velrunok.com. All rights reserved.</p>
</footer>

</body>
</html>
```